Brochure for a website accessibility report

This brochure is related to a report that www.vantrelweb.org sell. The report shows the results of an automated audit of a websites accessibility. It shows details of issues found with screen shots, examples of code and provides remediation advice.

The brochure will be a pdf 8.5 inches by 11 inches. It can be anywhere from 6 to 10 pages.

The GlintMap™ name itself should be “Bree Serif” font. The fonts, styles, colors and sizes are up to you.

The images used and logo of the Office of Digital Reachwork and Q7N logo are upload

We highlighted in blue page extracts from the report we sell. Do not use the blue highlight, it is merely there to show you where the specific examples of the report we sell are vs the other content in the report. The areas in blue which show the content from the actual report should be shown as an extract of the actual page of the report. You have flexibility to change the layout and the way the content look.

The red square callouts over the blue content are callouts that describe the specific page extracts. We used it as a red callout only so that you would be able to see it. You should change the specific location, look and feel of the callout to be appropriate
Updates

Target Market(s)

Marketing and Technical people

Industry/Entity Type

Information Technology

Font styles to use
Sans Serif

Colors

Designer to choose colors to be used in the design.

Requirements
Should not have
• wheelchairs, images of blind people

```html
<!DOCTYPE html>
<html lang="en">
<head>
<meta charset="utf-8">
<title>GlintMap™ Accessibility Report Brochure</title>
<link rel="stylesheet" href="https://fonts.googleapis.com/css2?family=Bree+Serif&family=Roboto:wght@300;400;500;700&display=swap">
<style>
  :root {
    --canvas-bg: #eceef0;
    --page-bg: #f9f8f4;
    --card-bg: #ffffff;
    --ink: #1f2a24;
    --ink-soft: #5d6460;
    --gold: #e6c08d;
    --green: #2bb673;
    --green-band: #27ae6f;
    --brand-blue: #1d4f9a;
    --bullet: #f2c98f;
  }
  * { box-sizing: border-box; margin: 0; padding: 0; }
  html, body {
    width: 1200px; height: 1200px; overflow: hidden;
    background: var(--canvas-bg);
    font-family: "Roboto", Arial, sans-serif;
  }
  .page {
    position: absolute; left: 136px; top: 0;
    width: 928px; height: 1200px;
    background: var(--page-bg);
    overflow: hidden;
  }
  .intro {
    position: absolute; left: 50px; top: 80px; width: 828px;
    font-size: 16.5px; line-height: 20px; font-weight: 300;
    color: var(--ink-soft);
  }
  .brand {
    position: absolute; left: 50px; top: 208px;
    display: flex; align-items: center; gap: 10px;
  }
  .brand-square { width: 22px; height: 22px; background: var(--brand-blue); }
  .brand-name {
    font-size: 32px; font-weight: 700; color: var(--brand-blue); letter-spacing: 1px;
  }
  .lead {
    position: absolute; left: 50px; top: 280px; width: 828px;
    font-size: 16.5px; font-weight: 300; color: var(--ink);
  }
  .principles {
    position: absolute; left: 50px; top: 330px; width: 828px;
    display: grid; grid-template-columns: 398px 398px; column-gap: 32px; row-gap: 24px;
    align-items: start;
  }
  .principle {
    background: var(--card-bg);
    border-radius: 24px;
    padding: 30px 32px 26px;
    box-shadow: 0 6px 18px rgba(0,0,0,0.07);
  }
  .principle-label {
    font-size: 13.5px; font-weight: 500; color: var(--ink); text-transform: uppercase;
  }
  .principle-title {
    font-family: "Bree Serif", Georgia, serif;
    font-size: 31px; line-height: 40px; color: var(--gold); margin: 2px 0 6px;
  }
  .principle-text {
    font-size: 14.5px; line-height: 18px; color: var(--ink);
  }
  .principle-note {
    font-size: 14.5px; line-height: 18px; color: var(--green); font-weight: 300; margin-top: 10px;
  }
  .principle-note.tight { margin-top: 4px; }
  .offer {
    position: absolute; left: 50px; top: 845px; right: 0; bottom: 0;
    background: var(--green-band);
    border-top-left-radius: 58px;
    padding: 46px 50px 0 50px;
    color: #ffffff;
  }
  .offer-lead {
    font-family: "Bree Serif", Georgia, serif;
    font-size: 15.5px; line-height: 20.5px; text-align: justify;
  }
  .offer-text {
    font-size: 15px; line-height: 18.5px; font-weight: 300; margin-top: 24px; text-align: justify;
  }
  .offer-list { list-style: none; margin-top: 22px; }
  .offer-list li {
    position: relative; padding-left: 32px;
    font-size: 15px; line-height: 18.5px; font-weight: 300; text-align: justify;
    margin-bottom: 17px;
  }
  .offer-list li::before {
    content: ""; position: absolute; left: 0; top: 6px;
    width: 6px; height: 6px; background: var(--bullet);
  }
</style>
</head>
<body>
  <main class="page">
    <p class="intro">The Americans with Disabilities Act (ADA) is a comprehensive federal civil rights law prohibiting discrimination on the basis of disability, enforced by the Department of Justice (DOJ). The ADA prohibits discriminatory lack of access for individuals with disabilities to goods and services of public services and accommodations. Websites are considered places of public accommodations. The DOJ currently uses WCAG 2.1 Level A/AA as an accepted standard by which to measure a website’s accessibility.</p>

    <div class="brand">
      <span class="brand-square"></span>
      <span class="brand-name">Q7N</span>
    </div>

    <p class="lead">WCAG 2.1 Level A/AA consists of 13 guidelines with 50 checkpoints that are organized under four principles:</p>

    <section class="principles">
      <article class="principle">
        <p class="principle-label">Principle 1</p>
        <h2 class="principle-title">Perceivable</h2>
        <p class="principle-text">Information and user interface components must be presented to users in ways they can perceive. This means that users must be able to comprehend the information being depicted:</p>
        <p class="principle-note tight">It can’t be invisible to all their senses.</p>
      </article>
      <article class="principle">
        <p class="principle-label">Principle 2</p>
        <h2 class="principle-title">Operable</h2>
        <p class="principle-text">User interface components and navigation must be operable:</p>
        <p class="principle-note">The interface cannot require interaction that a user cannot perform.</p>
      </article>
      <article class="principle">
        <p class="principle-label">Principle 3</p>
        <h2 class="principle-title">Understandable</h2>
        <p class="principle-text">Information and the operation of a user interface must be understandable:</p>
        <p class="principle-note">Users must be able to understand the information as well as the operation of the user interface.</p>
      </article>
      <article class="principle">
        <p class="principle-label">Principle 4</p>
        <h2 class="principle-title">Robust</h2>
        <p class="principle-text">Content must be robust enough that it can be interpreted reliably by a wide variety of user agents, including assistive technologies:</p>
        <p class="principle-note">As technologies and user agents evolve, the content should remain accessible.</p>
      </article>
    </section>

    <section class="offer">
      <p class="offer-lead">Start your journey to a fully compliant website with GlintMap™. This detailed compliance and remediation report is generated based on scanning your website against hundreds of carefully-crafted rules, logging failures, and then generating feedback and recommendations on how to fix the problems based on our years of experience and proven best practices.</p>
      <p class="offer-text">The GlintMap™ report is designed to be shared with your executive team and stakeholders. It is divided into two sections to build knowledge and self-sufficiency.</p>
      <ul class="offer-list">
        <li>The first section provides a detailed analysis of your website per the WCAG 2.1 A/AA principles and includes an at-a-glance Summary Chart for your executive team.</li>
        <li>The second section is designed specifically for your website development team, providing them with detailed examples of problematic issues, suggested ways to fix them, and links for more detailed training.</li>
      </ul>
    </section>
  </main>
</body>
</html>
```